Beautiful Quotes For Social Media Posts

We are looking for 5 beautifully designed quotes for our social media account.

Inspiration of styles we like in both style and color along with a few of our favorite fonts (you are NOT limited to these fonts this is just to give you an idea):
https://quillmorestudio.example.com/s/k7p2vx9tqa41mzn8wbd3ce6hr5lf0y2j

*These fonts are property of Quillmore Studio. You do not have permission/rights to use them outside of this assignment*

Quotes to use (5):
“Only those who dare to fail greatly can ever achieve greatly.” –Vernon T. Ashgrove
“Don’t go through life, grow through life.” – Milo Pendrake
“Follow your bliss and the universe will open doors where there were only walls.” – Arthur Venholm
“If you don’t like the road you’re walking, start paving another one.” – Greta Mossley
“Life is like riding a bicycle. To keep your balance, you must keep moving.” —Lucian Thornwick

File Specifics:
- JPG
- 10x10 in size (square)
- Please include @QuillmoreStudio in the bottom right left or center of each design

Brand Details:
Soft but rich pastel and bright colors.
Hand Drawn florals, doodles and art
Handwritten looking fonts
Artsy, Creative, Girl and Inspiring

```html
<!DOCTYPE html>
<html lang="en">
<head>
<meta charset="utf-8">
<title>Quote Post – Life is like riding a bicycle</title>
<link rel="stylesheet" href="https://fonts.googleapis.com/css2?family=Parisienne&family=Montserrat:wght@600&display=swap">
<style>
  :root {
    --wash-light: #f4f7fc;
    --wash-mid: #dbe5f6;
    --wash-deep: #b9cdee;
    --ink: #111111;
  }
  html, body {
    margin: 0;
    padding: 0;
    width: 1200px;
    height: 1200px;
    overflow: hidden;
    background: var(--wash-light);
  }
  .post {
    position: relative;
    width: 1200px;
    height: 1200px;
    overflow: hidden;
    background:
      radial-gradient(ellipse 520px 420px at 560px 640px, rgba(255,255,255,0.95), rgba(255,255,255,0) 70%),
      radial-gradient(ellipse 500px 400px at 80px 120px, var(--wash-mid), rgba(219,229,246,0) 70%),
      radial-gradient(ellipse 420px 380px at 1150px 700px, var(--wash-deep), rgba(185,205,238,0) 70%),
      radial-gradient(ellipse 460px 360px at 620px 1180px, var(--wash-mid), rgba(219,229,246,0) 70%),
      linear-gradient(160deg, #e4ecf9 0%, #f2f5fb 45%, #dde7f7 100%);
  }
  .decor {
    position: absolute;
    inset: 0;
    width: 1200px;
    height: 1200px;
  }
  .quote {
    position: absolute;
    left: 0;
    top: 428px;
    width: 1216px;
    margin: 0;
    text-align: center;
    font-family: "Parisienne", cursive;
    font-weight: 400;
    font-size: 90px;
    line-height: 134px;
    color: var(--ink);
  }
  .quote-line { display: block; }
  .attribution {
    position: absolute;
    left: 0;
    width: 1200px;
    top: 850px;
    margin: 0;
    text-align: center;
    font-family: "Parisienne", cursive;
    font-size: 46px;
    color: var(--ink);
  }
  .handle {
    position: absolute;
    left: 0;
    width: 1200px;
    top: 980px;
    margin: 0;
    text-align: center;
    font-family: "Montserrat", sans-serif;
    font-weight: 600;
    font-size: 29px;
    color: var(--ink);
  }
</style>
</head>
<body>
  <main class="post">
    <svg class="decor" viewBox="0 0 1200 1200" xmlns="http://www.w3.org/2000/svg">
      <defs>
        <radialGradient id="flora-fill" cx="50%" cy="50%" r="50%">
          <stop offset="0%" stop-color="#eef2fa" stop-opacity="0.95"/>
          <stop offset="70%" stop-color="#cfdbf0" stop-opacity="0.7"/>
          <stop offset="100%" stop-color="#c9d6ee" stop-opacity="0"/>
        </radialGradient>
      </defs>
      <ellipse class="flora flora-top-right" role="img" aria-label="Hand-drawn blue line-art lilies and leaves in the top right corner"
        cx="1000" cy="210" rx="260" ry="320" fill="url(#flora-fill)"/>
      <ellipse class="flora flora-bottom-left" role="img" aria-label="Hand-drawn blue line-art lilies and leaves in the bottom left corner"
        cx="200" cy="960" rx="300" ry="340" fill="url(#flora-fill)"/>
      <ellipse class="butterfly" role="img" aria-label="Hand-drawn blue line-art butterfly"
        cx="602" cy="224" rx="110" ry="122" fill="url(#flora-fill)"/>
    </svg>

    <p class="quote">
      <span class="quote-line">Life is like riding a bicycle.</span>
      <span class="quote-line">To keep your balance,</span>
      <span class="quote-line">you must keep moving</span>
    </p>

    <p class="attribution">— Lucian Thornwick</p>

    <p class="handle">@QuillmoreStudio</p>
  </main>
</body>
</html>
```